St Louis Electrician Needing a Business Card Design!!

We are a St Louis based electrical contracting firm that needs help designing a business card. We have a logo and I have another image that I would like to incorporate. Open to ideas..Thanks!!

Industry/Entity Type

Business

Requirements
Must have
• there are two downloads...one is the logo and the other is what i was wanting coming off the logo...the light rays. Like the logo with the blue background...Was thinking the whole card would be that color blue.
Should not have
• No lightning bolts

```html
<!DOCTYPE html>
<html lang="en">
<head>
<meta charset="utf-8">
<title>VoltaLine Inc. – Business Card</title>
<link rel="stylesheet" href="https://fonts.googleapis.com/css2?family=Lato:wght@300;400;700&display=swap">
<style>
  :root {
    --page-bg: #e9ebef;
    --card-navy: #1c284a;
    --card-navy-deep: #141d38;
    --card-navy-light: #2a3a66;
    --art-tone: #3c4775;
    --ink-white: #ffffff;
    --ink-soft: #e8ebf3;
  }
  * { box-sizing: border-box; margin: 0; padding: 0; }
  html, body {
    width: 1200px; height: 1200px; overflow: hidden;
    background: var(--page-bg);
    font-family: "Lato", Arial, sans-serif;
  }
  .stage {
    width: 1200px; height: 1200px;
    display: flex; align-items: center; justify-content: center;
  }
  .business-card {
    position: relative;
    width: 1160px; height: 679px;
    overflow: hidden;
    color: var(--ink-white);
    background:
      radial-gradient(ellipse 120px 80px at 12% 20%, var(--card-navy-light), transparent 70%),
      radial-gradient(ellipse 140px 90px at 40% 70%, var(--card-navy-light), transparent 70%),
      radial-gradient(ellipse 110px 70px at 70% 85%, var(--card-navy-light), transparent 70%),
      radial-gradient(ellipse 150px 100px at 25% 90%, var(--card-navy-deep), transparent 70%),
      var(--card-navy);
    box-shadow: 0 0 0 2px #55585f, 0 6px 18px rgba(0,0,0,0.25);
  }
  .ray-art {
    position: absolute; left: 36px; top: 40px;
    width: 1096px; height: 300px;
    background: linear-gradient(90deg, var(--card-navy) 0%, var(--art-tone) 100%);
    border-radius: 6px;
  }
  .brand-name {
    position: absolute; left: 600px; top: 268px;
    display: inline-block;
    font-weight: 400; font-size: 59px; letter-spacing: 0.5px;
    line-height: 1; color: var(--ink-white);
  }
  .brand-name .brand-suffix {
    display: block; text-align: right;
    font-size: 28px; margin-top: 2px;
  }
  .holder {
    position: absolute; left: 148px; width: 340px; top: 355px;
    text-align: center; line-height: 1.2;
  }
  .holder-name { font-weight: 700; font-size: 41px; }
  .holder-title { font-weight: 400; font-size: 35px; color: var(--ink-soft); }
  .contact-line {
    position: absolute;
    display: flex; align-items: flex-start;
    font-weight: 300; font-size: 33px; line-height: 42px;
    color: var(--ink-soft);
  }
  .contact-line svg { flex: none; margin-top: 4px; }
  .contact-address { left: 51px; top: 509px; gap: 24px; }
  .contact-address svg { width: 32px; height: 34px; }
  .contact-web { left: 47px; top: 593px; gap: 20px; }
  .contact-web svg { width: 40px; height: 36px; }
  .contact-phone { left: 604px; top: 533px; gap: 21px; }
  .contact-phone svg { width: 34px; height: 36px; }
  .contact-email { left: 598px; top: 592px; gap: 19px; }
  .contact-email svg { width: 42px; height: 34px; }
</style>
</head>
<body>
<main class="stage">
  <section class="business-card">
    <div class="ray-art" role="img" aria-label="Light rays streaming diagonally toward the company name"></div>

    <div class="brand-name">VoltaLine<span class="brand-suffix">Inc.</span></div>

    <div class="holder">
      <div class="holder-name">Joe Person</div>
      <div class="holder-title">President, CEO</div>
    </div>

    <div class="contact-line contact-address">
      <svg viewBox="0 0 24 24" aria-hidden="true"><path fill="#fff" d="M12 2a7 7 0 0 0-7 7c0 5 7 13 7 13s7-8 7-13a7 7 0 0 0-7-7zm0 9.5A2.5 2.5 0 1 1 12 6.5a2.5 2.5 0 0 1 0 5z"/></svg>
      <div>123 Main St<br>Yourtown, US, 12345</div>
    </div>

    <div class="contact-line contact-web">
      <svg viewBox="0 0 24 24" aria-hidden="true" fill="none" stroke="#fff" stroke-width="1.3"><circle cx="12" cy="12" r="10"/><ellipse cx="12" cy="12" rx="4.5" ry="10"/><path d="M2 12h20M4 7h16M4 17h16M12 2v20"/></svg>
      <div>www.gatewaycurrent.net</div>
    </div>

    <div class="contact-line contact-phone">
      <svg viewBox="0 0 24 24" aria-hidden="true" fill="none" stroke="#fff" stroke-width="1.8"><rect x="6.5" y="2" width="11" height="20" rx="2"/><path d="M6.5 17.5h11"/><circle cx="12" cy="19.8" r="0.6" fill="#fff"/></svg>
      <div>123-456-7890</div>
    </div>

    <div class="contact-line contact-email">
      <svg viewBox="0 0 24 24" aria-hidden="true" fill="none" stroke="#fff" stroke-width="1.5"><rect x="2" y="5" width="20" height="14"/><path d="M2 5l10 8 10-8M2 19l7.5-7.5M22 19l-7.5-7.5"/></svg>
      <div>jperson@gatewaycurrent.net</div>
    </div>
  </section>
</main>
</body>
</html>
```